Need sign/billboard help

I need somone to take my logo and turn it into a sign.
Needs to have: Bright Paws
Hound Play Lodge LLC
319-555-0187
Daycare - Boarding - Learning
Colors to use are in the pictures i included, however feel free to use different shades of gray. i Don't necessary want to background to be one solid color.
Also this sing will be a rectangle (4'x8')
Industry/Entity Type
Daycare
Look and feel
Each slider illustrates characteristics of the customer's brand and the style your logo design should communicate.

```html
<!DOCTYPE html>
<html lang="en">
<head>
<meta charset="utf-8">
<title>Bright Paws – Hound Play Lodge LLC Sign Concepts</title>
<link rel="stylesheet" href="https://fonts.googleapis.com/css2?family=Bebas+Neue&family=Oswald:wght@200;300&display=swap">
<style>
  :root {
    --lime: #acd037;
    --lime-light: #a9cf38;
    --lime-edge: #86a03a;
    --ink: #0b0b0b;
    --band-dark: #231f20;
    --band-gray: #808080;
    --tagline-gray: #8c8c8c;
    --white: #ffffff;
    --art-tone: rgba(0, 0, 0, 0.07);
  }
  * { box-sizing: border-box; margin: 0; padding: 0; }
  html, body { width: 1105px; height: 1200px; overflow: hidden; background: var(--white); }
  .canvas { position: relative; width: 1105px; height: 1200px; overflow: hidden; }

  .sign-field { position: absolute; left: 0; width: 1105px; overflow: hidden; }
  .sign-field--flat { top: 0; height: 437px; background: var(--lime); }
  .sign-field--glow {
    top: 648px; height: 434px;
    background: radial-gradient(ellipse at 45% 45%, var(--lime-light) 0%, #9fc238 45%, var(--lime-edge) 100%);
  }

  .mascot-art { position: absolute; border-radius: 40% 50% 6px 6px; background: var(--art-tone); }
  .sign-field--flat .mascot-art { left: 243px; top: 38px; width: 357px; height: 292px; }
  .sign-field--glow .mascot-art { left: 45px; top: 57px; width: 370px; height: 305px; }

  .brand-name {
    position: absolute;
    font-family: "Bebas Neue", sans-serif;
    font-weight: 400;
    color: var(--ink);
    letter-spacing: 3px;
    line-height: 1;
    white-space: nowrap;
  }
  .sign-field--flat .brand-name { left: 428px; top: 266px; font-size: 44px; }
  .sign-field--glow .brand-name { left: 234px; top: 296px; font-size: 48px; }

  .company-line {
    position: absolute; left: 0; right: 0; top: 350px;
    text-align: center;
    font-family: "Bebas Neue", sans-serif;
    font-weight: 400;
    font-size: 72px; line-height: 1;
    color: var(--ink);
    white-space: nowrap;
  }

  .company-stack {
    position: absolute; left: 730px; top: 80px; width: 335px;
    font-family: "Bebas Neue", sans-serif;
    font-weight: 400;
    color: var(--ink);
    line-height: 0.88;
  }
  .company-stack span { display: block; text-align: center; white-space: nowrap; }
  .company-stack .word-lead { font-size: 150px; }
  .company-stack .word-mid { font-size: 80px; }
  .company-stack .word-tail { font-size: 108px; }

  .info-band { position: absolute; left: 0; width: 1105px; height: 115px; display: flex; }
  .info-band--top { top: 437px; }
  .info-band--bottom { top: 1089px; height: 111px; }
  .services {
    width: 711px; background: var(--band-dark);
    display: flex; align-items: center; justify-content: center; gap: 22px;
    font-family: "Oswald", sans-serif; font-weight: 200;
    font-size: 50px; color: var(--tagline-gray);
    text-transform: uppercase; letter-spacing: 0;
  }
  .services .divider { width: 2px; height: 50px; background: var(--tagline-gray); }
  .phone {
    flex: 1; background: var(--band-gray);
    display: flex; align-items: center; justify-content: center;
    font-family: "Bebas Neue", sans-serif;
    font-size: 64px; color: var(--white); letter-spacing: 1px;
    white-space: nowrap;
  }
</style>
</head>
<body>
<main class="canvas">

  <section class="sign-field sign-field--flat">
    <div class="mascot-art" role="img" aria-label="Line illustration of a dog's head in profile"></div>
    <div class="brand-name">Bright Paws</div>
    <h1 class="company-line">Hound Play Lodge LLC</h1>
  </section>
  <div class="info-band info-band--top">
    <div class="services">
      <span>Daycare</span><span class="divider"></span>
      <span>Boarding</span><span class="divider"></span>
      <span>Learning</span>
    </div>
    <div class="phone">319-555-0187</div>
  </div>

  <section class="sign-field sign-field--glow">
    <div class="mascot-art" role="img" aria-label="Line illustration of a dog's head in profile"></div>
    <div class="brand-name">Bright Paws</div>
    <h2 class="company-stack">
      <span class="word-lead">Hound</span>
      <span class="word-mid">Play Lodge</span>
      <span class="word-tail">LLC</span>
    </h2>
  </section>
  <div class="info-band info-band--bottom">
    <div class="services">
      <span>Daycare</span><span class="divider"></span>
      <span>Boarding</span><span class="divider"></span>
      <span>Learning</span>
    </div>
    <div class="phone">319-555-0187</div>
  </div>

</main>
</body>
</html>
```